Project Management - Web Design Project

Vantrel 4 Management Limited is a company which provides specialist Project Control and Contract Management expertise to the Engineering, Construction and Manufacturing industries. The emphasis is on advanced Project Management techniques in particular Planning & Scheduling, Cost Control, Change Control, Risk Management, Reporting and Contract Administration. We are a global company (albeit a small start-up at this time) and pride ourselves on our ability to support projects to help them achieve their goals and objectives. Our aim is to implement work class control tools in a simple and user friendly manner. We would like the website to appear professional but at the same time easy to navigate and a good balance between text and pictures. The final design should communicate our value added service to our customers, our willingness to support and our structured approach to our work.

Target Market(s)

Project Management professionals working for engineering, construction and manufacturing organisations involved with delivering projects.

Industry/Entity Type

Construction

Requirements
Must have
• The website must include all of the content from the attached Excel brief. The company logo (attached) must also be included in the design. The design must portray a professional look and feel. Please include pictures and photographs related to project management in the engineering, construction and manufacturing industries. We may supplement with pictures of our own during the next steps.
Nice to have
• Emphasis that Vantrel 4 is available to support, guide, direct to achieve positive outcomes for the projects. We work hard at developing our customer relationships. Our employees are experienced in advanced project management techniques.
Should not have
• The design should not use old style fonts. It should look modern and professional. Do not include cartoons or silly illustrations.

```html
<!DOCTYPE html>
<html lang="en">
<head>
<meta charset="utf-8">
<title>Vantrel 4 Management Limited</title>
<link rel="stylesheet" href="https://fonts.googleapis.com/css2?family=Roboto+Condensed:wght@400;700&display=swap">
<style>
  :root {
    --page-bg: #f6f6f6;
    --page-bg-dark: #e4e4e4;
    --brand-grey: #6b6b6b;
    --brand-dot: #2a63b8;
    --link-ink: #1a1a1a;
    --icon-blue: #1d4f9c;
    --nav-blue-top: #2a6cc2;
    --nav-blue-bottom: #0c3c85;
    --nav-divider: #8fb3e6;
    --home-tab-top: #ffffff;
    --home-tab-bottom: #d9dde3;
    --paper-white: #f4f4f4;
    --paper-grey: #cfcfcf;
    --shadow-grey: #8a8a8a;
    --suit-dark: #2c2c2c;
  }
  * { box-sizing: border-box; margin: 0; padding: 0; }
  html, body { width: 1200px; height: 863px; overflow: hidden; }
  body {
    position: relative;
    font-family: "Roboto Condensed", Arial, sans-serif;
    background: radial-gradient(ellipse at 20% 20%, #ffffff 0%, var(--page-bg) 45%, var(--page-bg-dark) 100%);
  }
  .header-decor {
    position: absolute; left: 620px; top: 110px; width: 580px; height: 300px;
    background:
      linear-gradient(172deg, rgba(255,255,255,0) 30%, rgba(190,190,190,0.45) 42%, rgba(255,255,255,0) 54%),
      linear-gradient(168deg, rgba(255,255,255,0) 55%, rgba(200,200,200,0.4) 66%, rgba(255,255,255,0) 78%),
      radial-gradient(circle at 92% 60%, rgba(180,180,180,0.35) 0 12%, rgba(255,255,255,0) 30%);
    -webkit-mask-image: linear-gradient(90deg, transparent 0%, #000 35%);
    mask-image: linear-gradient(90deg, transparent 0%, #000 35%);
  }
  .utility-nav { position: absolute; top: 18px; left: 808px; display: flex; gap: 42px; }
  .utility-nav a {
    display: flex; align-items: center; gap: 10px;
    color: var(--link-ink); text-decoration: underline; font-size: 25px; text-transform: uppercase;
  }
  .utility-nav svg { width: 22px; height: 20px; fill: var(--icon-blue); }
  .brand { position: absolute; left: 135px; top: 112px; width: 300px; }
  .brand-dot {
    width: 140px; height: 140px; border-radius: 50%; margin-left: 70px;
    background: var(--brand-dot);
  }
  .brand-name {
    margin-top: 8px; color: var(--brand-grey); font-weight: 400;
    font-size: 44px; line-height: 42px; letter-spacing: 4px; text-transform: uppercase;
  }
  .brand-name span { display: block; font-size: 19px; line-height: 22px; letter-spacing: 2.6px; }
  .main-nav {
    position: absolute; left: 271px; top: 412px; height: 63px; width: 940px;
    display: flex; overflow: hidden; isolation: isolate;
  }
  .main-nav .tab {
    position: relative; height: 63px; display: flex; align-items: center; justify-content: center;
    color: #fff; font-size: 24px; text-transform: uppercase; text-decoration: none; white-space: nowrap;
  }
  .main-nav .tab::before {
    content: ""; position: absolute; inset: 0 -12px; z-index: -1;
    transform: skewX(-22deg);
    background: linear-gradient(var(--nav-blue-top), var(--nav-blue-bottom));
    border-left: 2px solid var(--nav-divider);
  }
  .main-nav .tab-home { width: 62px; }
  .main-nav .tab-home::before { background: linear-gradient(var(--home-tab-top), var(--home-tab-bottom)); border-left: none; inset: 0 -12px 0 -30px; }
  .main-nav .tab-home svg { width: 28px; height: 26px; fill: var(--icon-blue); }
  .tab-about { width: 196px; }
  .tab-intro { width: 222px; }
  .tab-control { width: 262px; }
  .tab-contract { width: 240px; justify-content: flex-start; padding-left: 26px; }
  .hero-photo {
    position: absolute; left: 130px; top: 475px; width: 1070px; height: 388px;
    background:
      radial-gradient(ellipse 30% 55% at 92% 45%, rgba(30,30,30,0.9) 0%, rgba(60,60,60,0.6) 45%, rgba(60,60,60,0) 100%),
      radial-gradient(ellipse 22% 35% at 68% 95%, rgba(40,40,40,0.55) 0%, rgba(40,40,40,0) 100%),
      radial-gradient(ellipse 45% 70% at 40% 70%, var(--paper-white) 0%, rgba(244,244,244,0) 70%),
      linear-gradient(170deg, #e2e2e2 0%, var(--paper-grey) 30%, #dadada 55%, var(--shadow-grey) 85%, var(--suit-dark) 100%);
  }
  .slider-prev {
    position: absolute; left: 130px; top: 740px; width: 82px; height: 82px;
    background: rgba(255,255,255,0.75); border: none;
    display: flex; align-items: center; justify-content: center;
  }
  .slider-prev svg { width: 30px; height: 50px; }
</style>
</head>
<body>
  <div class="header-decor" aria-hidden="true"></div>

  <nav class="utility-nav">
    <a href="#"><svg viewBox="0 0 22 20"><path d="M11 1 1 10h3v9h5v-6h4v6h5v-9h3z"/></svg>Home</a>
    <a href="#"><svg viewBox="0 0 22 20"><path d="M1 3h20v14H1z"/><path d="M1 3l10 8 10-8" fill="none" stroke="#fff" stroke-width="2"/></svg>Contact Us</a>
  </nav>

  <div class="brand">
    <div class="brand-dot" aria-hidden="true"></div>
    <p class="brand-name">Vantrel 4<span>Management Limited</span></p>
  </div>

  <nav class="main-nav">
    <a class="tab tab-home" href="#" aria-label="Home"><svg viewBox="0 0 22 20"><path d="M11 1 1 10h3v9h5v-6h4v6h5v-9h3z"/></svg></a>
    <a class="tab tab-about" href="#">About Us</a>
    <a class="tab tab-intro" href="#">Introduction</a>
    <a class="tab tab-control" href="#">Project Control</a>
    <a class="tab tab-contract" href="#">Contract Management</a>
  </nav>

  <div class="hero-photo" role="img" aria-label="Black and white photograph of a hand holding a pen over a binder with a project report of tables and bar charts"></div>
  <button class="slider-prev" aria-label="Previous slide">
    <svg viewBox="0 0 30 50"><path d="M26 3 4 25l22 22" fill="none" stroke="#8a8a8a" stroke-width="3"/></svg>
  </button>
</body>
</html>
```